Horseriders ecommerce

I need the design of a web site and ecommerce for horse riders product. the actual site is brinamarket.it and is completely to rebuild.
the most important thing that must come out from the design is that this shop sells products for both type of riding: english and western and as well has products available and good for both. (accessories and horse care)
the site owners loves much more the western riding and they want to gain a good part of customers of it, that's why i ask you to give the central area and importance to the western products.
at http://www.keltorange.com you can see a site style that we like, especially for the inner pages of products.
colors and graphics elements must be related to the world of horse riding, but we want the design to keep elegance and style, without being so western!
you need to find a way to create a cool design, user friendly to buy and that gives the real impression of professionality and care.
please check this site: http://www.pemblyworks.it/
the style is not so nice in my opinion, but somehow the navigation is friendly
in attachment to the project I add the mockup of the home page. Abou the inner page, please feel free to create the correct layout and check the one of www.keltorange.com which I like especially for the product sheet.

p.s. you can change the color of the logo
Updates

Hello dear designers,
i've pushed a little the deadline.
I will give you feedback in a while.
thaks to all
Ginevra

Target Market(s)

horse riders
western riders
english riders
stables owners

Industry/Entity Type

Product

Requirements
Must have
• style, elegance and western atmosphere. GOOD SPACES to show products.
• MUST HAVE a base way to manage banners in home page
Nice to have
• images of horses, but the most important images are products
Should not have
• too many western elements

```html
<!DOCTYPE html>
<html lang="en">
<head>
<meta charset="utf-8">
<title>Ardena Riding – Horse Riding Shop</title>
<link rel="stylesheet" href="https://fonts.googleapis.com/css2?family=Open+Sans:wght@400;600;700&family=Roboto+Slab:wght@400;700&family=Oswald:wght@400;500&display=swap">
<style>
:root{
  --red:#d5232f;
  --ink:#2b2b2b;
  --muted:#7a7a7a;
  --line:#dcdcdc;
  --panel:#ffffff;
  --foot:#ececec;
  --band:#3a3a3a;
}
*{margin:0;padding:0;box-sizing:border-box}
html,body{width:729px;height:1200px;overflow:hidden}
body{font-family:"Open Sans",sans-serif;color:var(--ink);
  background:linear-gradient(180deg,#c9d3da 0%,#b9c4bb 40%,#9fa98c 70%,#8d8f74 100%)}
.page{position:relative;width:729px;height:1200px}
.sheet{position:absolute;left:22px;top:0;width:685px;height:1200px;background:var(--panel)}
.abs{position:absolute}

.topbar{left:22px;top:0;width:685px;height:24px;border-bottom:1px solid var(--line);
  font-size:7.5px;color:var(--muted);display:flex;justify-content:space-between;align-items:center;padding:0 22px;text-transform:uppercase}
.topbar .call b{color:var(--red);font-weight:600}
.topbar .links span{margin-left:12px}

.social{left:44px;top:38px;display:flex;gap:5px}
.social i{display:block;width:20px;height:20px;border-radius:50%;border:1.5px solid #8a8a8a}
.brand{left:279px;top:44px;width:171px;height:40px;display:flex;align-items:center;justify-content:center;gap:6px}
.brand .dot{width:12px;height:12px;border-radius:50%;background:var(--red);flex:none}
.brand .name{font-family:"Roboto Slab",Georgia,serif;font-weight:700;font-size:15px;color:var(--red);white-space:nowrap}
.cart{left:628px;top:42px;display:flex;gap:6px;align-items:flex-start;font-size:8px;color:var(--muted)}
.cart b{display:block;color:var(--red);font-weight:600;font-size:9px}

.nav{left:44px;top:110px;width:641px;height:24px;border-bottom:1px solid var(--line);
  display:flex;justify-content:center;align-items:center;font-size:8.5px;letter-spacing:.3px;text-transform:uppercase}
.nav a{color:var(--ink);text-decoration:none;padding:0 11px;border-left:1px solid #bbb;line-height:10px}
.nav a:first-child{border-left:0}
.nav a.active{color:var(--red)}

.hero{left:44px;top:160px;width:641px;height:272px;
  background:linear-gradient(100deg,#6f8f46 0%,#9db76a 30%,#5a3a22 55%,#7a4b2b 75%,#3f5a2c 100%)}
.arrow{top:282px;width:14px;height:28px;background:rgba(255,255,255,.85);display:flex;align-items:center;justify-content:center}

.promo{top:450px;height:66px;background:var(--band);color:#fff;text-align:center;
  display:flex;flex-direction:column;justify-content:center;border:2px solid #fff;outline:1px solid #999}
.promo h2{font-family:"Oswald",sans-serif;font-weight:400;font-size:30px;line-height:30px;letter-spacing:1px}
.promo p{font-size:7px;letter-spacing:.5px;text-transform:uppercase;margin-top:3px;color:#ddd}

.section-title{left:44px;top:550px;width:641px;display:flex;align-items:center;gap:12px;
  font-family:"Oswald",sans-serif;font-weight:400;font-size:16px;letter-spacing:.5px;text-transform:uppercase}
.section-title::before,.section-title::after{content:"";flex:1;height:1px;background:var(--line)}
.category{top:586px;width:206px}
.category .shot{height:192px}
.category h3{font-family:"Roboto Slab",Georgia,serif;font-size:12px;font-weight:700;margin-top:12px;white-space:nowrap}
.category p{font-size:7.5px;line-height:11px;color:var(--muted);margin-top:5px}
.category a{display:block;font-size:8px;color:var(--red);margin-top:5px;text-decoration:none}

.quote{left:22px;top:884px;width:685px;height:80px;text-align:center;border-top:1px solid var(--line)}
.quote .text{display:block;font-family:"Roboto Slab",Georgia,serif;font-size:27px;margin-top:16px}
.quote .who{display:block;font-family:"Roboto Slab",Georgia,serif;font-size:11px;color:var(--red);margin-top:2px}

.footer{left:22px;top:966px;width:685px;height:208px;background:var(--foot)}
.col{top:988px}
.col h4{font-family:"Oswald",sans-serif;font-weight:400;font-size:13px;text-transform:uppercase;margin-bottom:10px;letter-spacing:.3px}
.col p{font-size:7.5px;line-height:11px;color:var(--muted)}
.footer-brand{display:flex;align-items:center;gap:5px;margin-bottom:10px}
.footer-brand .dot{width:10px;height:10px;border-radius:50%;background:var(--red);flex:none}
.footer-brand .name{font-family:"Roboto Slab",Georgia,serif;font-weight:700;font-size:12px;color:var(--red);white-space:nowrap}
.tags{display:flex;flex-wrap:wrap;gap:4px;width:140px}
.tags span{background:var(--red);color:#fff;font-size:6.5px;text-transform:uppercase;padding:3px 5px}
.recent{display:flex;gap:8px;margin-bottom:10px}
.recent .thumb{width:46px;height:42px;background:#d6d6d6;flex:none}
.recent p{font-size:7px;line-height:10px}
.recent b{display:block;color:var(--red);font-size:8.5px;margin-top:4px}

.bottom{left:22px;top:1174px;width:685px;height:26px;display:flex;justify-content:space-between;align-items:center;padding:0 22px;font-size:7.5px;color:var(--muted)}
.pay{display:flex;gap:4px}
.pay i{display:block;width:26px;height:15px;border:1px solid #bbb;background:#f4f4f4;border-radius:2px}
</style>
</head>
<body>
<div class="page">
  <div class="sheet"></div>

  <div class="abs topbar">
    <div class="call">In case of any questions, call this number: <b>+00 000 000</b></div>
    <div class="links"><span>Wishlist</span><span>My account</span><span>Cart</span></div>
  </div>

  <div class="abs social" aria-label="Social links"><i></i><i></i><i></i><i></i><i></i></div>

  <div class="abs brand"><span class="dot"></span><span class="name">Ardena Riding</span></div>

  <div class="abs cart">
    <svg width="16" height="18" viewBox="0 0 16 18"><path d="M2 5h12l-1 12H3z" fill="#333"/><path d="M5 5V3a3 3 0 0 1 6 0v2" fill="none" stroke="#333" stroke-width="1.3"/></svg>
    <div>ITEMS (0)<b>£0</b></div>
  </div>

  <nav class="abs nav">
    <a class="active" href="#">Home</a><a href="#">Our Products</a><a href="#">How to Buy</a><a href="#">Who We Are</a><a href="#">Offers</a><a href="#">Cart</a><a href="#">Contact</a>
  </nav>

  <div class="abs hero" role="img" aria-label="Young rider in helmet beside her horse with a red saddle pad"></div>
  <div class="abs arrow" style="left:44px"><svg width="6" height="10" viewBox="0 0 6 10"><path d="M5 1 1 5l4 4" fill="none" stroke="#555" stroke-width="1.4"/></svg></div>
  <div class="abs arrow" style="left:671px"><svg width="6" height="10" viewBox="0 0 6 10"><path d="M1 1l4 4-4 4" fill="none" stroke="#555" stroke-width="1.4"/></svg></div>

  <div class="abs promo" style="left:44px;width:308px">
    <h2>FREE SHIPPING</h2>
    <p>When your order is above 75$</p>
  </div>
  <div class="abs promo" style="left:368px;width:317px">
    <h2>THE BEST DEALS</h2>
    <p>With us the best deals on every riding season</p>
  </div>

  <h2 class="abs section-title">Our Product Categories</h2>

  <div class="abs category" style="left:44px">
    <div class="shot" role="img" aria-label="Stable block with horses in a paddock" style="background:linear-gradient(180deg,#9fb3c4 0%,#8a6a4d 55%,#6b5a3e 100%)"></div>
    <h3>English Riders &amp; Horses</h3>
    <p>Lorem ipsum dolor sit amet, consectetur adipiscing elit sed do eiusmod tempor.</p>
    <a href="#">View the Category</a>
  </div>
  <div class="abs category" style="left:262px">
    <div class="shot" role="img" aria-label="Dressage rider in tailcoat on a dark horse" style="background:linear-gradient(180deg,#b9c6cf 0%,#4a4a52 50%,#2e2a28 100%)"></div>
    <h3>Western Rider &amp; Horses</h3>
    <p>Lorem ipsum dolor sit amet, consectetur adipiscing elit sed do eiusmod tempor.</p>
    <a href="#">View the Category</a>
  </div>
  <div class="abs category" style="left:479px">
    <div class="shot" role="img" aria-label="Show jumper on a chestnut horse clearing a fence" style="background:linear-gradient(180deg,#9a3b2e 0%,#7b4a2c 45%,#6f8a4a 100%)"></div>
    <h3>Accessories and House Care</h3>
    <p>Lorem ipsum dolor sit amet, consectetur adipiscing elit sed do eiusmod tempor.</p>
    <a href="#">View the Category</a>
  </div>

  <div class="abs quote">
    <span class="text">“Customer Feedbak Goes Here”</span>
    <span class="who">- Happy Customer</span>
  </div>

  <div class="abs footer"></div>

  <div class="abs col" style="left:44px;width:150px">
    <div class="footer-brand"><span class="dot"></span><span class="name">Ardena Riding</span></div>
    <p>Text of the printing and typesetting industry. Lorem Ipsum has been the industry's standard dummy text ever since the 1500s.</p>
  </div>

  <div class="abs col" style="left:207px">
    <h4>Tag Cloud</h4>
    <div class="tags">
      <span>Saddles</span><span>Bridles</span><span>Boots</span><span>Helmets</span><span>Spurs</span><span>Blankets</span><span>Grooming</span><span>Chaps</span><span>Reins</span><span>Pads</span><span>Gloves</span><span>Halters</span><span>Bits</span><span>Ropes</span>
    </div>
  </div>

  <div class="abs col" style="left:365px;width:135px">
    <h4>Get In Touch</h4>
    <p>Text of the printing and typesetting industry. Lorem Ipsum has been the industry's standard dummy text ever since the 1500s.</p>
  </div>

  <div class="abs col" style="left:522px;width:165px">
    <h4>Recent Product</h4>
    <div class="recent"><div class="thumb" role="img" aria-label="Product photo"></div><p>Has been the industry's standard<b>£100</b></p></div>
    <div class="recent"><div class="thumb" role="img" aria-label="Product photo"></div><p>Has been the industry's standard<b>£60.00</b></p></div>
  </div>

  <div class="abs bottom">
    <div class="pay" aria-label="Accepted payments"><i></i><i></i><i></i><i></i><i></i></div>
    <div>All Rights Reserved</div>
  </div>
</div>
</body>
</html>
```